KVM Contracting services . Building and maintenance services, optic fibre installation

Business cards and logo design.I need a logo that I can use on business cards ,workwear and on my vehicles. I would like the KVM to be the main or larger text and contracting services to be the smaller or less important text.I like monograms, modern designs and repeating patterns symbols. I am also a Gemini and my favourite number is 22 so if this can be any inspiration to help with the design. Am thinking of the using German flag colours as a his is my family’s heritage. And the other 2 main colours I wear is black and white.But any ideas are appreciated.I do not need a design that is trade specific but a design that could be used for any business.

Target Market(s)

General public

Contact Information for Business Card

KVM Contracting Services ( front of business card)

(Back of business card)
Marcus Dellwood
0419274530
Maintenance services
Optic fibre and data installation

Logo Text

Logo can just be pattern or monogram or incorporate KVM . I like the gemini star sign and the number 22

Colors
ec1f27
000000
fbee3e
ffffff

Requirements
Must have
• Logo and KVM Contracting Services on the front of business card
Nice to have
• Possible use of German flag colours.
• Modern design.
• Design to be able to be used on black or white background as I want to put it on clothing

```html
<!DOCTYPE html>
<html lang="en">
<head>
<meta charset="utf-8">
<title>KVM Contracting Services – Business Card</title>
<link href="https://fonts.googleapis.com/css2?family=Poppins:wght@500;600&display=swap" rel="stylesheet">
<style>
  :root {
    --backdrop: #8b8b79;
    --card-white: #ffffff;
    --card-dark: #222528;
    --brand-red: #d9272a;
    --brand-yellow: #f2c400;
  }
  * { margin: 0; padding: 0; box-sizing: border-box; }
  html, body {
    width: 1200px;
    height: 1200px;
    overflow: hidden;
    background: var(--backdrop);
    font-family: "Poppins", sans-serif;
  }
  .canvas {
    position: relative;
    width: 1200px;
    height: 1200px;
  }
  .card {
    position: absolute;
    left: 237px;
    width: 726px;
    height: 416px;
    border-radius: 22px;
  }
  .card--front {
    top: 142px;
    background: var(--card-white);
  }
  .card--back {
    top: 641px;
    background: var(--card-dark);
  }
  .wordmark {
    position: absolute;
    left: 131px;
    top: 118px;
    width: 492px;
    height: 200px;
  }
  .wordmark text {
    fill: var(--brand-red);
    font-family: "Poppins", sans-serif;
    font-weight: 600;
  }
  .contact {
    position: absolute;
    left: 107px;
    top: 126px;
    list-style: none;
    font-weight: 500;
    font-size: 32px;
    line-height: 41px;
    color: var(--brand-yellow);
  }
  .contact__name { color: var(--brand-red); }
</style>
</head>
<body>
<main class="canvas">
  <section class="card card--front" aria-label="Card front">
    <svg class="wordmark" viewBox="0 0 492 200" role="img" aria-label="KVM Contracting Services">
      <text x="0" y="153" font-size="170" textLength="492" lengthAdjust="spacingAndGlyphs">KVM</text>
      <text x="0" y="196" font-size="27" textLength="492" lengthAdjust="spacing">CONTRACTING SERVICES</text>
    </svg>
  </section>

  <section class="card card--back" aria-label="Card back">
    <ul class="contact">
      <li class="contact__name">Marcus Dellwood</li>
      <li class="contact__phone">0419274530</li>
      <li class="contact__service">Maintenance services</li>
      <li class="contact__service">Optic fibre and data installation</li>
    </ul>
  </section>
</main>
</body>
</html>
```